Business Card Design

Business Card for professional consulting firm working with large financial institutions.

Target Market(s)

Executive buyers

Industry/Entity Type

Banking

Contact Information for Business Card

Mild creativity wanted. Not boring, but do elaborate artwork.

Font styles to use
Serif
Sans Serif

Colors

Designer to choose colors to be used in the design.

Requirements
Must have
• Standard business card features - company name, individual name, telephone, website, email, locations.
Nice to have
• Two colors
Should not have
• too many colors, fancy printing, cartoons.

```html
<!DOCTYPE html>
<html lang="en">
<head>
<meta charset="utf-8">
<title>Business Card – Front and Back</title>
<link rel="stylesheet" href="https://fonts.googleapis.com/css2?family=Open+Sans:wght@300;400&display=swap">
<style>
  :root {
    --backdrop: #2a2a2a;
    --card-white: #ffffff;
    --brand-red: #b5081f;
    --charcoal: #3b3b3b;
    --ink: #111111;
  }
  * { box-sizing: border-box; margin: 0; padding: 0; }
  html, body {
    width: 1200px;
    height: 1200px;
    overflow: hidden;
    background: var(--backdrop);
  }
  .canvas {
    position: relative;
    width: 1200px;
    height: 1200px;
  }
  .card {
    position: absolute;
    left: 180px;
    width: 840px;
    height: 480px;
    background: var(--card-white);
    overflow: hidden;
    box-shadow: 0 14px 40px rgba(0,0,0,0.45);
  }
  .card--front { top: 90px; }
  .card--back  { top: 630px; }

  /* Front: band along the bottom edge */
  .name-band {
    position: absolute;
    left: 0; right: 0; bottom: 0;
    height: 112px;
    display: flex;
  }
  .name-band__accent { width: 190px; background: var(--brand-red); }
  .name-band__plate {
    flex: 1;
    background: var(--charcoal);
    display: flex;
    align-items: center;
    justify-content: center;
  }
  .owner-name {
    font-family: "Open Sans", sans-serif;
    font-weight: 300;
    font-size: 44px;
    color: var(--ink);
    letter-spacing: 0.5px;
    white-space: nowrap;
  }

  .contact-icon {
    position: absolute;
    width: 44px;
    height: 44px;
  }
  .contact-icon--email { left: 64px;  top: 60px; }
  .contact-icon--phone { left: 196px; top: 60px; }
  .contact-icon--web   { left: 486px; top: 60px; }

  .brand-name {
    position: absolute;
    font-family: "Open Sans", sans-serif;
    font-weight: 400;
    color: var(--ink);
    text-transform: uppercase;
    letter-spacing: 3px;
    white-space: nowrap;
  }
  .card--front .brand-name {
    right: 70px;
    top: 196px;
    font-size: 40px;
  }

  /* Back: band along the right edge */
  .edge-band {
    position: absolute;
    top: 0; right: 0; bottom: 0;
    width: 112px;
    display: flex;
    flex-direction: column;
  }
  .edge-band__accent { height: 150px; background: var(--brand-red); }
  .edge-band__plate  { flex: 1; background: var(--charcoal); }

  .card--back .brand-name {
    left: 0;
    width: 728px;
    top: 200px;
    text-align: center;
    font-size: 56px;
    line-height: 1.2;
  }
</style>
</head>
<body>
<main class="canvas">

  <section class="card card--front" aria-label="Card front">
    <svg class="contact-icon contact-icon--email" viewBox="0 0 44 44" aria-label="Email">
      <rect x="4" y="10" width="36" height="24" fill="var(--ink)"/>
      <polyline points="4,10 22,25 40,10" fill="none" stroke="#fff" stroke-width="2"/>
    </svg>
    <svg class="contact-icon contact-icon--phone" viewBox="0 0 44 44" aria-label="Telephone">
      <path d="M6 16 Q22 4 38 16 L34 22 L28 18 L28 14 Q22 12 16 14 L16 18 L10 22 Z" fill="var(--ink)"/>
      <rect x="10" y="22" width="24" height="16" rx="3" fill="var(--ink)"/>
      <circle cx="22" cy="30" r="4" fill="#fff"/>
    </svg>
    <svg class="contact-icon contact-icon--web" viewBox="0 0 44 44" aria-label="Website">
      <g fill="none" stroke="var(--ink)" stroke-width="2">
        <circle cx="22" cy="22" r="17"/>
        <ellipse cx="22" cy="22" rx="7" ry="17"/>
        <line x1="5" y1="22" x2="39" y2="22"/>
        <line x1="8" y1="13" x2="36" y2="13"/>
        <line x1="8" y1="31" x2="36" y2="31"/>
      </g>
    </svg>

    <p class="brand-name">Halden Partners</p>

    <div class="name-band">
      <div class="name-band__accent"></div>
      <div class="name-band__plate"><p class="owner-name">NAME of Owner</p></div>
      <div class="name-band__accent"></div>
    </div>
  </section>

  <section class="card card--back" aria-label="Card back">
    <p class="brand-name">Halden Partners</p>
    <div class="edge-band">
      <div class="edge-band__accent"></div>
      <div class="edge-band__plate"></div>
      <div class="edge-band__accent"></div>
    </div>
  </section>

</main>
</body>
</html>
```